"Eyebrow Threading Flyer Design"

We need a flyer design for a new service that will be provided in our established Beauty Salon in Toorak called "Threading". We provide all beauty services for our clients & would like to now introduce this very popular ancient method of hair removal.
Following are four "40% Off Threading Combo Packages" that will hopefully tempt new clients into our salon.
#Package 1- Eyebrow Threading plus Eyebrow Tint or Eyelash Tint Normally $53 Now $32
#Package 2- Eyebrow Threading plus Full Set Mink Lash Extensions
Normally $208 Now $125
#Package 3- Eyebrow Threading plus Glossa Manicure Or Pedicure
Normally $128 Now $77
#Package 4- Eyebrow Threading plus Collagen Facial
Normally $148 Now $89
We would like to see designs that use pink with whit or black to suit logo & business name & final design should be girly/feminine 7 fun.
On the back we would like the following details:
Velvet Dawn Beauty, "Lindell Court", shop 7, 418 Marlowe Street, 3187
Tel: 03 9471 2360, Email: info@velvetdawnbeauty.example, Web: www.velvetdawnbeauty.example
A map of exact location and business hours:
Mon 9am to 5pm, Tue 9am to 6pm, Wed 9am to 6pm, Thu 9am to 8pm, Fri 9am to 6pm, sat 9am to 5pm

Target Market(s)

Women between the ages of 20 to 60 years of age

Industry/Entity Type

Hair

Font styles to use
Script

Colors
e34297
000000

Requirements
Must have
• Pink and black or pink and white colors
Should not have
• Fake looking eyelashes displayed

```html
<!DOCTYPE html>
<html lang="en">
<head>
<meta charset="utf-8">
<title>Velvet Dawn Beauty – Threading Flyer</title>
<link rel="stylesheet" href="https://fonts.googleapis.com/css2?family=Arimo:wght@400;700&display=swap">
<style>
  :root {
    --pink: #e34297;
    --pink-soft: #f27dbb;
    --ink: #231b22;
    --ink-deep: #1a1419;
    --white: #ffffff;
    --stage: #ece8ea;
    --map-land: #ece6d8;
    --map-road: #d9cfb8;
  }
  * { box-sizing: border-box; margin: 0; padding: 0; }
  html, body { width: 1200px; height: 900px; overflow: hidden; }
  body {
    background: var(--stage);
    font-family: "Arimo", Arial, sans-serif;
    position: relative;
  }
  .flyer {
    position: absolute;
    top: 90px;
    width: 470px;
    height: 720px;
    background: var(--white);
    box-shadow: 0 6px 18px rgba(0,0,0,0.18);
  }
  .flyer--front { left: 95px; padding: 8px; }
  .flyer--back { left: 635px; padding: 8px; }

  /* Front */
  .front-grid {
    position: relative;
    width: 100%;
    height: 100%;
  }
  .tile { position: absolute; }
  .photo-nails {
    left: 0; top: 0; width: 190px; height: 215px;
    background: linear-gradient(135deg, #f6e4e4 0%, #e9b9b8 50%, #c53a3e 100%);
  }
  .photo-eye {
    left: 0; top: 219px; width: 190px; height: 300px;
    background: linear-gradient(160deg, #e8c3ad 0%, #b98470 45%, #5a3a36 70%, #a8203a 100%);
  }
  .brand-block {
    left: 0; top: 523px; width: 190px; height: 181px;
    background: var(--pink);
    display: flex; flex-direction: column; align-items: center; justify-content: center;
    gap: 14px;
    padding: 0 8px;
  }
  .brand-name {
    color: var(--white);
    font-size: 17px;
    font-weight: 400;
    text-align: center;
    letter-spacing: 1px;
    line-height: 1.2;
  }
  .brand-square {
    width: 70px; height: 70px;
    background: var(--white);
  }
  .offer-panel {
    left: 194px; top: 0; width: 260px; height: 500px;
    background: var(--ink);
    color: var(--white);
    text-align: center;
    padding: 22px 10px 0;
  }
  .offer-kicker {
    color: var(--pink);
    font-size: 18px;
    letter-spacing: 3px;
    line-height: 1.2;
  }
  .offer-title {
    font-size: 17px;
    line-height: 1.15;
    margin-bottom: 18px;
  }
  .package { font-size: 12.5px; line-height: 1.2; margin-bottom: 17px; }
  .package-label, .package-now { color: var(--pink); }
  .photo-feet {
    left: 194px; top: 504px; width: 260px; height: 200px;
    background: linear-gradient(170deg, #3a2d2a 0%, #e3b19c 40%, #d99585 70%, #e34297 100%);
  }

  /* Back */
  .back-panel {
    position: relative;
    width: 100%; height: 100%;
    background: var(--ink);
    overflow: hidden;
    color: var(--white);
    text-align: center;
  }
  .back-wave { position: absolute; left: 0; top: 0; }
  .back-content { position: relative; padding-top: 26px; }
  .back-name { color: var(--pink); font-size: 20px; }
  .back-address { font-size: 20px; line-height: 1.2; }
  .map-area {
    margin: 18px auto 0;
    width: 400px; height: 150px;
    border: 3px solid var(--pink);
    background: linear-gradient(120deg, var(--map-land), var(--map-road));
  }
  .contact { margin-top: 34px; font-size: 18px; line-height: 1.2; }
  .contact-label { color: var(--pink); }
  .hours-title { margin-top: 24px; color: var(--pink); font-size: 18px; }
  .hours-list { margin-top: 16px; list-style: none; font-size: 18px; line-height: 1.15; }
  .back-brand {
    position: absolute; left: 0; bottom: 0; width: 100%; height: 140px;
    display: flex; align-items: center; gap: 28px; padding-left: 34px;
  }
  .back-square { width: 90px; height: 90px; background: var(--white); flex: none; }
  .back-brand-name { color: var(--ink); font-size: 28px; line-height: 1.15; text-align: left; letter-spacing: 1px; }
</style>
</head>
<body>

<section class="flyer flyer--front" aria-label="Front of flyer">
  <div class="front-grid">
    <div class="tile photo-nails" role="img" aria-label="Photo of manicured hands with red nail polish"></div>
    <div class="tile photo-eye" role="img" aria-label="Close-up photo of a made-up eye and red nails"></div>
    <div class="tile brand-block">
      <div class="brand-name">Velvet Dawn Beauty</div>
      <div class="brand-square"></div>
    </div>
    <div class="tile offer-panel">
      <p class="offer-kicker">WE OFFER</p>
      <p class="offer-title">four "40% Off<br>Threading Combo Packages</p>
      <div class="package">
        <p class="package-label">#Package 1</p>
        <p>Eyebrow Threading plus Eyebrow Tint or Eyelash Tint</p>
        <p>Normally $53</p>
        <p class="package-now">Now $32</p>
      </div>
      <div class="package">
        <p class="package-label">#Package 2</p>
        <p>Eyebrow Threading plus Full Set Mink Lash Extensions</p>
        <p>Normally $208</p>
        <p class="package-now">Now $125</p>
      </div>
      <div class="package">
        <p class="package-label">#Package 3</p>
        <p>Eyebrow Threading plus Glossa Manicure Or Pedicure</p>
        <p>Normally $128</p>
        <p class="package-now">Now $77</p>
      </div>
      <div class="package">
        <p class="package-label">#Package 4</p>
        <p>Eyebrow Threading plus<br>Collagen Facial</p>
        <p>Normally $148</p>
        <p class="package-now">Now $89</p>
      </div>
    </div>
    <div class="tile photo-feet" role="img" aria-label="Photo of pedicured feet on pebbles with pink petals"></div>
  </div>
</section>

<section class="flyer flyer--back" aria-label="Back of flyer">
  <div class="back-panel">
    <svg class="back-wave" width="454" height="704" viewBox="0 0 454 704" aria-hidden="true">
      <path d="M0 510 C120 470 300 400 454 370 L454 704 L0 704 Z" fill="var(--pink)"/>
    </svg>
    <div class="back-content">
      <p class="back-name">Velvet Dawn Beauty</p>
      <p class="back-address">"Lindell Court", shop 7,<br>418 Marlowe Street, 3187</p>
      <div class="map-area" role="img" aria-label="Street map showing the salon location"></div>
      <p class="contact"><span class="contact-label">Tel:</span> 03 9471 2360<br>
        <span class="contact-label">Email:</span> info@velvetdawnbeauty.example<br>
        <span class="contact-label">Web:</span> www.velvetdawnbeauty.example</p>
      <p class="hours-title">Bussiness hours:</p>
      <ul class="hours-list">
        <li>Monday: 9am to 5pm</li>
        <li>Tuesday: 9am to 6pm</li>
        <li>Wednesday: 9am to 6pm</li>
        <li>Thursday: 9am to 8pm</li>
        <li>Friday: 9am to 6pm</li>
        <li>Saturday: 9am to 5pm</li>
      </ul>
    </div>
    <div class="back-brand">
      <div class="back-square"></div>
      <p class="back-brand-name">Velvet Dawn<br>Beauty</p>
    </div>
  </div>
</section>

</body>
</html>
```